Statement on the current financial and economic crisis, with a focus on Greece,

Anybody can become angry - that is easy, but to be angry with the right person and to the right degree and at the right time and for the right purpose, and in the right way - that is not within everybody's power and is not easy.
(Kelphinor ) greek philosopher

i want to do a poster with this words from Kelphinor greek philosopher and to show this statement for the greek people... its about for my project that i am doing.

Target Market(s)

my audience will be greek people but not only, from 18-80 years old for that reason i want my statement to be in english.

Industry/Entity Type

Financial

Requirements
Must have
• Anybody can become angry - that is easy, but to be angry with the right person and to the right degree and at the right time and for the right purpose, and in the right way - that is not within everybody's power and is not easy.
i want to show in my poster this statement from:
Kelphinor greek philosopher (384 – 322 BC)

```html
<!DOCTYPE html>
<html lang="en">
<head>
<meta charset="utf-8">
<title>Kelphinor – On Anger</title>
<link rel="stylesheet" href="https://fonts.googleapis.com/css2?family=Heebo:wght@700;800&display=swap">
<style>
  :root {
    --poster-red: #ee1b3c;
    --panel-glow: #fff3a0;
    --panel-mid: #fcd37a;
    --panel-edge: #fbb560;
    --ink: #231f20;
    --frame: #262626;
    --portrait-bg: #000000;
    --portrait-stone: #cfcfcf;
    --ornament-tone: #1a1a1a;
  }
  * { margin: 0; padding: 0; box-sizing: border-box; }
  html, body {
    width: 849px;
    height: 1200px;
    overflow: hidden;
  }
  body {
    background: var(--poster-red);
    font-family: "Heebo", "Helvetica Neue", Arial, sans-serif;
    color: var(--ink);
  }
  .poster {
    position: relative;
    width: 849px;
    height: 1200px;
    background: var(--poster-red);
  }
  .quote-panel {
    position: absolute;
    left: 78px;
    top: 96px;
    width: 692px;
    height: 1007px;
    border: 3px solid var(--frame);
    background: radial-gradient(ellipse 60% 55% at 47% 52%, var(--panel-glow) 0%, var(--panel-mid) 45%, var(--panel-edge) 100%);
  }
  .quote {
    position: absolute;
    left: 0;
    top: 50px;
    width: 100%;
    text-align: center;
    font-weight: 700;
    font-size: 36.5px;
    line-height: 68px;
    letter-spacing: 0.1px;
    padding-left: 0;
  }
  .portrait {
    position: absolute;
    left: 103px;
    top: 744px;
    width: 170px;
    height: 255px;
    background: radial-gradient(ellipse 45% 50% at 50% 40%, var(--portrait-stone) 0%, #8a8a8a 55%, var(--portrait-bg) 100%);
  }
  .attribution {
    position: absolute;
    left: 270px;
    top: 828px;
    width: 330px;
    text-align: center;
    font-weight: 700;
  }
  .attribution .name {
    font-size: 37px;
    line-height: 48px;
  }
  .attribution .role,
  .attribution .dates {
    font-size: 27px;
    line-height: 35px;
  }
  .ornament {
    position: absolute;
    left: 590px;
    top: 1015px;
    width: 180px;
    height: 170px;
    border-radius: 50%;
    background: radial-gradient(circle at 50% 50%, rgba(26,26,26,0.35) 0%, rgba(26,26,26,0.12) 55%, rgba(26,26,26,0) 72%);
  }
</style>
</head>
<body>
  <main class="poster">
    <section class="quote-panel">
      <p class="quote">
        Anybody can become angry<br>
        - that is easy, but to be<br>
        angry with the right person<br>
        and to the right degree and<br>
        at the right time and for the<br>
        right purpose, and in the<br>
        right way - that is not<br>
        within everybody's power<br>
        and is not easy.
      </p>
      <div class="portrait" role="img" aria-label="Marble bust of the philosopher Kelphinor on a black background"></div>
      <div class="attribution">
        <p class="name">Kelphinor</p>
        <p class="role">Greek Philosopher</p>
        <p class="dates">(384 – 322 BC)</p>
      </div>
    </section>
    <div class="ornament" role="img" aria-label="Black and silver flourish ornament at the panel corner"></div>
  </main>
</body>
</html>
```